Create a Dynamic, Connecting, Professional looking PowerPoint Design master for our company.

Power point design

Target Market: High worth individuals and corporate group
Industry: Sport and services

Landscape format

Should include various slide such as:
Introduction page (photo background- inclusive logo)
Company presentation (with photos of various projects)
Different slide layouts to place general information with large photo & logo (in different sizes) as well as standard elements, such as text boxes, lines, default shapes, etc
Timeline page
Table pages
Various infographic style pages with editable chart
Our service page – Icons
Location page (world map)
Comparaison pages (3 offers to compare)
Closing page – thank you & contact
Page numbering

Colors:
#6ea6fa
#517ed8
#3758b4
#203390
#060d6c
#2EC193
White / Grey and black

Fonts:
Work sans / Helveticanow / Or other suitable.
Creative use of the logo in the slides. The Trelum icon may be used as a small device or large watermark to enhance branding.

The uploaded photos are indicative of the ones that we would like to use (ie: sail racing) there are here for you to include in the design but would need to be easily replaceable by the final photos we would be using.

If you have any questions or need any aditional material, please send me a message and I will try to respond to it as quickly as possible (bearing in mind that my time zone is UTC +2)

Target Market(s)

High worth individuals and corporate groups

Industry/Entity Type

Sport and services (sailing)

Font styles to use
Other font styles liked:
• Work Sans / Helveticanow

Colors
0054AA
0677BA
7BADD7
CADEEF
E8F1F8
00AB8E
00BBA5
67D7C9
C6EFE9
E9F9F6

Requirements
Must have
• Introduction page (photo background- inclusive logo) Company presentation (with photos of various projects) Different slide layouts to place general information with large photo & logo (in different sizes) as well as standard elements, such as text boxes, lines, default shapes, etc Timeline page Table pages Various infographic style pages with editable chart Our service page – Icons Location page (world map) Comparaison pages (3 offers to compare) Closing page – thank you & contact Page numbering
Nice to have
• Creative use of the logo in the slides. The Trelum icon may be used as a small device or large watermark to enhance branding.

```html
<!DOCTYPE html>
<html lang="en">
<head>
<meta charset="utf-8">
<title>Trelum – Presentation Master</title>
<link href="https://fonts.googleapis.com/css2?family=Work+Sans:wght@300;400;500;600;700;800&display=swap" rel="stylesheet">
<style>
:root{
  --sky:#6ea6fa;
  --blue:#517ed8;
  --royal:#3758b4;
  --navy:#203390;
  --ink:#060d6c;
  --pale:#e8f1f8;
  --mist:#cadeef;
  --canvas:#d4d6d9;
  --text:#4a4f5c;
  --white:#ffffff;
}
*{box-sizing:border-box;margin:0;padding:0}
html,body{width:1200px;height:4120px;overflow:hidden}
body{background:var(--canvas);font-family:"Work Sans",Arial,sans-serif;color:var(--text);position:relative}

.top-brand{position:absolute;top:52px;right:60px;display:flex;align-items:center;gap:10px;font-weight:800;font-size:34px;letter-spacing:2px;color:var(--ink)}
.top-brand .mark{width:26px;height:26px;border-radius:50%;background:var(--ink)}

.hero{position:absolute;left:240px;top:150px;width:720px;height:405px;box-shadow:0 18px 40px rgba(0,0,0,.25)}
.hero .slide{transform:scale(1.2857);transform-origin:0 0}

.deck{position:absolute;left:32px;top:740px;display:grid;grid-template-columns:560px 560px;grid-auto-rows:315px;column-gap:16px;row-gap:20px}
.slide{position:relative;width:560px;height:315px;background:var(--white);overflow:hidden}
.slide.wide{grid-column:1/-1;justify-self:center}
.slide > *{position:absolute}

.photo{background:linear-gradient(180deg,#8cb4de 0%,#4f7fb8 45%,#1f4a86 100%)}
.photo.crew{background:linear-gradient(160deg,#b9c4d1 0%,#7d8ea5 55%,#3e5370 100%)}
.photo.race{background:linear-gradient(180deg,#9fc0dd 0%,#6c8fae 50%,#35557a 100%)}
.photo.mono{background:linear-gradient(180deg,#c9cbcf 0%,#8d9097 60%,#55585f 100%)}
.photo.map{background:linear-gradient(180deg,#eef1f6,#dfe5ee)}

.brand{display:flex;align-items:center;gap:5px;font-weight:800;letter-spacing:1px;color:var(--ink)}
.brand i{display:block;border-radius:50%;background:var(--ink)}
.brand.lg{font-size:20px}.brand.lg i{width:14px;height:14px}
.brand.sm{font-size:8px}.brand.sm i{width:6px;height:6px}
.brand.light{color:var(--white)}.brand.light i{background:var(--white)}
.foot{left:14px;bottom:9px}
.pgnum{right:12px;bottom:8px;width:12px;height:12px;border-radius:50%;background:var(--blue);color:var(--white);font-size:6px;font-weight:600;display:flex;align-items:center;justify-content:center}

.kicker{font-weight:800;color:var(--ink);text-transform:uppercase;line-height:1.05}
.accent{font-weight:400;color:var(--blue)}
.copy{font-size:6px;line-height:1.5;color:var(--text)}
.copy.light{color:#dfe7fb}
.btn{height:12px;background:var(--blue);color:var(--white);font-size:5.5px;font-weight:600;display:flex;align-items:center;justify-content:center}
.bracket{width:26px;height:26px;border-top:4px solid var(--blue);border-right:4px solid var(--blue)}

.svc-icon{width:30px;height:30px;border-radius:50%;border:1.5px solid var(--white);display:flex;align-items:center;justify-content:center}
.col-title{font-size:7px;font-weight:700;color:var(--ink);text-align:center}

.table{border-collapse:collapse;font-size:6px}
.table th{background:var(--navy);color:var(--white);padding:5px 6px;font-weight:600;text-align:left}
.table th.yr{background:var(--blue);text-align:center}
.table td{padding:4px 6px;border-bottom:1px solid #e3e7ef}
.table td.n{text-align:center}
.table tr.total td{background:var(--navy);color:var(--white);font-weight:600}

.stat{background:var(--white);border:1px solid var(--mist);display:flex;flex-direction:column;justify-content:center;padding-left:12px}
.stat b{font-size:18px;color:var(--blue);font-weight:700}
.stat span{font-size:5.5px}

.card{border-radius:8px 8px 0 0;background:var(--navy);color:var(--white);text-align:center}
.card .num{width:38px;height:38px;border-radius:50%;border:1.5px solid var(--white);margin:18px auto 10px;display:flex;align-items:center;justify-content:center;font-size:18px;font-weight:700}
.card h4{font-size:7px;font-weight:700}
.card h5{font-size:6px;font-weight:400;color:var(--sky);margin-bottom:8px}
</style>
</head>
<body>

<div class="top-brand"><span class="mark"></span>TRELUM</div>

<div class="hero">
  <section class="slide">
    <div class="photo" role="img" aria-label="Racing catamarans sailing on open blue water" style="left:0;top:0;width:330px;height:315px;clip-path:polygon(0 0,100% 0,78% 100%,0 100%)"></div>
    <svg style="left:230px;top:180px" width="120" height="135" viewBox="0 0 120 135"><polygon points="100,0 120,0 80,135 58,135" fill="#6ea6fa"/><polygon points="70,60 84,60 62,135 48,135" fill="#517ed8"/></svg>
    <div class="brand lg" style="left:372px;top:62px"><i></i>TRELUM</div>
    <div class="kicker" style="left:372px;top:112px;font-size:22px">Presentation</div>
    <div class="accent" style="left:372px;top:138px;font-size:19px">Title Goes Here</div>
    <p class="copy" style="left:372px;top:168px;width:160px">Lorem ipsum dolor sit amet, consectetur adipiscing elit. Vivamus lacus nisi, cursus et eleifend quis, commodo id lorem.</p>
    <div class="btn" style="left:440px;top:215px;width:90px">Subtitle goes here</div>
    <div class="pgnum">1</div>
  </section>
</div>

<main class="deck">

  <section class="slide">
    <div class="photo" role="img" aria-label="Racing catamarans sailing on open blue water" style="left:0;top:0;width:330px;height:315px;clip-path:polygon(0 0,100% 0,78% 100%,0 100%)"></div>
    <svg style="left:230px;top:180px" width="120" height="135" viewBox="0 0 120 135"><polygon points="100,0 120,0 80,135 58,135" fill="#6ea6fa"/><polygon points="70,60 84,60 62,135 48,135" fill="#517ed8"/></svg>
    <div class="brand lg" style="left:372px;top:62px"><i></i>TRELUM</div>
    <div class="kicker" style="left:372px;top:112px;font-size:22px">Presentation</div>
    <div class="accent" style="left:372px;top:138px;font-size:19px">Title Goes Here</div>
    <p class="copy" style="left:372px;top:168px;width:160px">Lorem ipsum dolor sit amet, consectetur adipiscing elit. Vivamus lacus nisi, cursus et eleifend quis, commodo id lorem.</p>
    <div class="btn" style="left:440px;top:215px;width:90px">Subtitle goes here</div>
    <div class="pgnum">1</div>
  </section>

  <section class="slide">
    <div class="photo crew" role="img" aria-label="Sailing crew working the deck of a racing yacht" style="left:0;top:0;width:330px;height:315px;clip-path:polygon(0 0,100% 0,78% 100%,0 100%)"></div>
    <svg style="left:230px;top:180px" width="120" height="135" viewBox="0 0 120 135"><polygon points="100,0 120,0 80,135 58,135" fill="#6ea6fa"/><polygon points="70,60 84,60 62,135 48,135" fill="#517ed8"/></svg>
    <div class="brand lg" style="left:372px;top:62px"><i></i>TRELUM</div>
    <div class="kicker" style="left:372px;top:112px;font-size:22px">Presentation</div>
    <div class="accent" style="left:372px;top:138px;font-size:19px">Title Goes Here</div>
    <p class="copy" style="left:372px;top:168px;width:160px">Lorem ipsum dolor sit amet, consectetur adipiscing elit. Vivamus lacus nisi, cursus et eleifend quis, commodo id lorem.</p>
    <div class="btn" style="left:440px;top:215px;width:90px">Subtitle goes here</div>
    <div class="pgnum">2</div>
  </section>

  <section class="slide">
    <div class="photo" role="img" aria-label="Fleet of racing yachts under sail" style="left:0;top:0;width:560px;height:190px"></div>
    <div class="kicker" style="left:0;top:208px;width:560px;text-align:center;font-size:15px">Heading <span class="accent" style="text-transform:none">Goes Here</span></div>
    <p class="copy" style="left:90px;top:232px;width:380px;text-align:center">Lorem ipsum dolor sit amet, consectetur adipiscing elit. Vivamus lacus nisi, cursus et eleifend quis, commodo id lorem. Sed feugiat felis vitae ligula posuere, at dictum magna porta. Nunc tempus arcu in turpis aliquet.</p>
    <div class="brand sm foot"><i></i>TRELUM</div>
    <div class="pgnum">3</div>
  </section>

  <section class="slide">
    <div class="kicker" style="left:24px;top:58px;font-size:15px">Venenatis:</div>
    <div class="accent" style="left:24px;top:76px;font-size:14px">Dolor Sit Amet</div>
    <p class="copy" style="left:24px;top:104px;width:190px">Lorem ipsum dolor sit amet, consectetur adipiscing elit. Vivamus lacus nisi, cursus et eleifend quis, commodo id lorem. Sed feugiat felis vitae ligula posuere.</p>
    <p class="copy" style="left:24px;top:150px;width:190px">Nunc tempus arcu in turpis aliquet, sed pretium justo lacinia. Donec vitae mauris at nibh ultrices tincidunt.</p>
    <div class="photo" role="img" aria-label="Racing yachts heeling in the wind" style="left:236px;top:44px;width:300px;height:220px"></div>
    <div class="bracket" style="right:14px;top:30px"></div>
    <div class="brand sm foot"><i></i>TRELUM</div>
    <div class="pgnum">4</div>
  </section>

  <section class="slide">
    <div style="left:0;top:0;width:560px;height:150px;background:var(--navy)"></div>
    <div style="left:0;top:22px;width:560px;text-align:center;font-size:14px;font-weight:800;color:#fff">Our <span style="color:var(--sky)">SERVICE</span></div>
    <div class="svc-icon" style="left:125px;top:70px"><svg width="14" height="14" viewBox="0 0 14 14"><path d="M7 1v10M2 11h10L7 1z" stroke="#fff" fill="none" stroke-width="1.2"/></svg></div>
    <div class="svc-icon" style="left:265px;top:70px"><svg width="14" height="14" viewBox="0 0 14 14"><circle cx="7" cy="7" r="5" stroke="#fff" fill="none" stroke-width="1.2"/><path d="M7 4v3l2 2" stroke="#fff" fill="none" stroke-width="1.2"/></svg></div>
    <div class="svc-icon" style="left:405px;top:70px"><svg width="14" height="14" viewBox="0 0 14 14"><path d="M7 13s4-4.5 4-7.5a4 4 0 0 0-8 0C3 8.5 7 13 7 13z" stroke="#fff" fill="none" stroke-width="1.2"/><circle cx="7" cy="5.5" r="1.4" fill="#fff"/></svg></div>
    <div class="col-title" style="left:80px;top:172px;width:120px">HEADING GOES HERE</div>
    <div class="col-title" style="left:220px;top:172px;width:120px">HEADING GOES HERE</div>
    <div class="col-title" style="left:360px;top:172px;width:120px">HEADING GOES HERE</div>
    <p class="copy" style="left:85px;top:188px;width:110px;text-align:center">Lorem ipsum dolor sit amet, consectetur adipiscing elit nisi cursus.</p>
    <p class="copy" style="left:225px;top:188px;width:110px;text-align:center">Lorem ipsum dolor sit amet, consectetur adipiscing elit nisi cursus.</p>
    <p class="copy" style="left:365px;top:188px;width:110px;text-align:center">Lorem ipsum dolor sit amet, consectetur adipiscing elit nisi cursus.</p>
    <div class="brand sm foot"><i></i>TRELUM</div>
    <div class="pgnum">5</div>
  </section>

  <section class="slide">
    <div class="kicker" style="left:24px;top:40px;font-size:15px">Venenatis:</div>
    <div class="accent" style="left:24px;top:58px;font-size:14px">Dolor Sit Amet</div>
    <p class="copy" style="left:24px;top:86px;width:180px">Lorem ipsum dolor sit amet, consectetur adipiscing elit. Vivamus lacus nisi, cursus et eleifend quis, commodo id lorem.</p>
    <p class="copy" style="left:24px;top:124px;width:180px">Sed feugiat felis vitae ligula posuere, at dictum magna porta.</p>
    <div class="photo" role="img" aria-label="Yachts sailing near a coastline" style="left:220px;top:30px;width:150px;height:235px"></div>
    <div class="photo crew" role="img" aria-label="Sailor trimming a sail on deck" style="left:376px;top:30px;width:164px;height:235px"></div>
    <div class="brand sm foot"><i></i>TRELUM</div>
    <div class="pgnum">6</div>
  </section>

  <section class="slide">
    <div class="kicker" style="left:24px;top:22px;font-size:14px">Company <span class="accent" style="text-transform:none">Presentation</span></div>
    <div style="left:0;top:60px;width:560px;height:200px;background:var(--pale)"></div>
    <p class="copy" style="left:24px;top:80px;width:120px">Lorem ipsum dolor sit amet, consectetur adipiscing elit. Vivamus lacus nisi, cursus et eleifend quis.</p>
    <div class="photo race" role="img" aria-label="Project one: foiling race yacht" style="left:160px;top:78px;width:118px;height:100px"></div>
    <div class="photo" role="img" aria-label="Project two: regatta fleet start" style="left:290px;top:78px;width:118px;height:100px"></div>
    <div class="photo" role="img" aria-label="Project three: catamaran racing" style="left:420px;top:78px;width:118px;height:100px"></div>
    <div class="btn" style="left:160px;top:184px;width:118px;height:28px;background:var(--blue)">TITLE GOES HERE</div>
    <div class="btn" style="left:290px;top:184px;width:118px;height:28px;background:var(--royal)">TITLE GOES HERE</div>
    <div class="btn" style="left:420px;top:184px;width:118px;height:28px;background:var(--navy)">TITLE GOES HERE</div>
    <div class="brand sm foot"><i></i>TRELUM</div>
    <div class="pgnum">7</div>
  </section>

  <section class="slide">
    <div style="left:0;top:0;width:210px;height:150px;background:var(--navy)"></div>
    <div style="left:20px;top:28px;font-size:13px;font-weight:800;color:#fff;line-height:1.1">LOREM IPSUM<br><span style="font-weight:400;color:var(--sky)">Dolor Sit Amet,<br>Consectetur</span></div>
    <p class="copy light" style="left:20px;top:98px;width:170px">Vivamus lacus nisi, cursus et eleifend quis, commodo id lorem.</p>
    <p class="copy" style="left:20px;top:170px;width:170px">Lorem ipsum dolor sit amet, consectetur adipiscing elit. Sed feugiat felis vitae ligula posuere, at dictum magna porta.</p>
    <div style="left:210px;top:0;width:350px;height:265px;background:var(--blue)"></div>
    <div style="left:226px;top:22px;width:320px;display:flex;flex-direction:column;gap:16px">
      <div style="display:flex;gap:10px;align-items:center"><span class="svc-icon" style="position:static;width:24px;height:24px;flex:none"></span><span class="copy light"><b style="color:#fff">HEADING GOES HERE</b><br>Lorem ipsum dolor sit amet, consectetur elit.</span></div>
      <div style="display:flex;gap:10px;align-items:center"><span class="svc-icon" style="position:static;width:24px;height:24px;flex:none"></span><span class="copy light"><b style="color:#fff">HEADING GOES HERE</b><br>Lorem ipsum dolor sit amet, consectetur elit.</span></div>
      <div style="display:flex;gap:10px;align-items:center"><span class="svc-icon" style="position:static;width:24px;height:24px;flex:none"></span><span class="copy light"><b style="color:#fff">HEADING GOES HERE</b><br>Lorem ipsum dolor sit amet, consectetur elit.</span></div>
      <div style="display:flex;gap:10px;align-items:center"><span class="svc-icon" style="position:static;width:24px;height:24px;flex:none"></span><span class="copy light"><b style="color:#fff">HEADING GOES HERE</b><br>Lorem ipsum dolor sit amet, consectetur elit.</span></div>
    </div>
    <div class="brand sm foot"><i></i>TRELUM</div>
    <div class="pgnum">8</div>
  </section>

  <section class="slide">
    <div class="kicker" style="left:24px;top:40px;font-size:15px">Venenatis:</div>
    <div class="accent" style="left:24px;top:58px;font-size:14px">Dolor Sit Amet</div>
    <p class="copy" style="left:24px;top:86px;width:150px">Lorem ipsum dolor sit amet, consectetur adipiscing elit. Vivamus lacus nisi, cursus et eleifend quis.</p>
    <div style="left:0;top:180px;width:190px;height:85px;background:var(--mist)"></div>
    <div class="photo mono" role="img" aria-label="Regatta fleet seen from above" style="left:190px;top:20px;width:120px;height:245px"></div>
    <div class="photo race" role="img" aria-label="Race yachts with colourful sails" style="left:314px;top:20px;width:110px;height:245px"></div>
    <div class="photo" role="img" aria-label="Foiling yacht at speed" style="left:428px;top:20px;width:112px;height:245px"></div>
    <div class="brand sm foot"><i></i>TRELUM</div>
    <div class="pgnum">9</div>
  </section>

  <section class="slide">
    <div class="photo race" role="img" aria-label="Race yachts on the start line" style="left:20px;top:20px;width:150px;height:245px"></div>
    <div class="photo mono" role="img" aria-label="Crowded regatta fleet" style="left:174px;top:20px;width:110px;height:245px"></div>
    <div class="photo" role="img" aria-label="Sailboats with numbered sails" style="left:288px;top:20px;width:100px;height:245px"></div>
    <div class="kicker" style="left:402px;top:60px;font-size:14px">Venenatis:</div>
    <div class="accent" style="left:402px;top:77px;font-size:13px">Dolor Sit Amet</div>
    <p class="copy" style="left:402px;top:102px;width:140px">Lorem ipsum dolor sit amet, consectetur adipiscing elit. Vivamus lacus nisi, cursus et eleifend quis, commodo id lorem.</p>
    <div class="brand sm foot"><i></i>TRELUM</div>
    <div class="pgnum">10</div>
  </section>

  <section class="slide">
    <div class="photo" role="img" aria-label="Trimaran racing under a cloudy sky" style="left:0;top:20px;width:330px;height:245px"></div>
    <div class="kicker" style="left:352px;top:70px;font-size:15px">Venenatis:</div>
    <div class="accent" style="left:352px;top:88px;font-size:14px">Dolor Sit Amet</div>
    <p class="copy" style="left:352px;top:114px;width:180px">Lorem ipsum dolor sit amet, consectetur adipiscing elit. Vivamus lacus nisi, cursus et eleifend quis, commodo id lorem.</p>
    <div class="bracket" style="right:14px;top:14px"></div>
    <div class="brand sm foot"><i></i>TRELUM</div>
    <div class="pgnum">11</div>
  </section>

  <section class="slide">
    <div class="photo" role="img" aria-label="Trimaran sailing past a headland" style="left:0;top:20px;width:200px;height:245px"></div>
    <div class="photo race" role="img" aria-label="Race boat foiling above the water" style="left:204px;top:20px;width:160px;height:245px"></div>
    <div class="kicker" style="left:380px;top:70px;font-size:14px">Venenatis:</div>
    <div class="accent" style="left:380px;top:87px;font-size:13px">Dolor Sit Amet</div>
    <p class="copy" style="left:380px;top:112px;width:160px">Lorem ipsum dolor sit amet, consectetur adipiscing elit. Vivamus lacus nisi, cursus et eleifend quis.</p>
    <div class="bracket" style="right:14px;top:14px"></div>
    <div class="brand sm foot"><i></i>TRELUM</div>
    <div class="pgnum">12</div>
  </section>

  <section class="slide">
    <div class="kicker" style="left:24px;top:22px;font-size:14px">Timeline <span class="accent" style="text-transform:none">Slide</span></div>
    <svg style="left:24px;top:60px" width="512" height="150" viewBox="0 0 512 150">
      <line x1="0" y1="100" x2="512" y2="100" stroke="#cadeef" stroke-width="2"/>
      <g fill="#517ed8"><circle cx="60" cy="100" r="4"/><circle cx="190" cy="100" r="4"/><circle cx="320" cy="100" r="4"/><circle cx="450" cy="100" r="4"/></g>
      <g stroke="#517ed8"><line x1="60" y1="100" x2="60" y2="30"/><line x1="190" y1="100" x2="190" y2="60"/><line x1="320" y1="100" x2="320" y2="30"/><line x1="450" y1="100" x2="450" y2="60"/></g>
      <g font-size="7" font-family="Work Sans" fill="#203390" font-weight="700"><text x="50" y="118">2019</text><text x="180" y="118">2020</text><text x="310" y="118">2021</text><text x="440" y="118">2022</text></g>
    </svg>
    <p class="copy" style="left:92px;top:80px;width:100px"><b>LOREM IPSUM DOLOR</b><br>Consectetur adipiscing elit vivamus.</p>
    <p class="copy" style="left:222px;top:110px;width:100px"><b>LOREM IPSUM DOLOR</b><br>Consectetur adipiscing elit vivamus.</p>
    <p class="copy" style="left:352px;top:80px;width:100px"><b>LOREM IPSUM DOLOR</b><br>Consectetur adipiscing elit vivamus.</p>
    <p class="copy" style="left:482px;top:110px;width:70px"><b>LOREM IPSUM</b><br>Consectetur elit.</p>
    <div class="brand sm foot"><i></i>TRELUM</div>
    <div class="pgnum">13</div>
  </section>

  <section class="slide">
    <div class="kicker" style="left:24px;top:22px;font-size:14px">Table <span class="accent" style="text-transform:none">Slide</span></div>
    <table class="table" style="left:24px;top:55px;width:512px">
      <tr><th>HEADING Goes Here</th><th class="yr">2020</th><th class="yr">2021</th><th class="yr">2022</th></tr>
      <tr><td>Lorem ipsum dolor sit</td><td class="n">120</td><td class="n">150</td><td class="n">180</td></tr>
      <tr><td>Consectetur adipiscing</td><td class="n">90</td><td class="n">110</td><td class="n">140</td></tr>
      <tr><td>Vivamus lacus nisi</td><td class="n">75</td><td class="n">95</td><td class="n">120</td></tr>
      <tr><td>Cursus et eleifend</td><td class="n">60</td><td class="n">80</td><td class="n">105</td></tr>
      <tr><td>Commodo id lorem</td><td class="n">45</td><td class="n">70</td><td class="n">90</td></tr>
      <tr><td>Sed feugiat felis</td><td class="n">30</td><td class="n">55</td><td class="n">75</td></tr>
      <tr class="total"><td>Total</td><td class="n">420</td><td class="n">560</td><td class="n">710</td></tr>
    </table>
    <div class="brand sm foot"><i></i>TRELUM</div>
    <div class="pgnum">14</div>
  </section>

  <section class="slide">
    <div class="kicker" style="left:24px;top:22px;font-size:14px">Chart <span class="accent" style="text-transform:none">Slide</span></div>
    <svg style="left:200px;top:70px" width="160" height="160" viewBox="-80 -80 160 160">
      <path d="M0 0 L0 -70 A70 70 0 0 1 66.6 -21.6 Z" fill="#6ea6fa"/>
      <path d="M0 0 L66.6 -21.6 A70 70 0 0 1 -15.5 68.3 Z" fill="#3758b4"/>
      <path d="M0 0 L-15.5 68.3 A70 70 0 0 1 -66.6 -21.6 Z" fill="#517ed8"/>
      <path d="M0 0 L-66.6 -21.6 A70 70 0 0 1 0 -70 Z" fill="#203390"/>
    </svg>
    <div style="left:40px;top:80px;font-size:20px;font-weight:700;color:var(--blue)">25%</div>
    <p class="copy" style="left:40px;top:106px;width:110px">Lorem ipsum dolor sit amet consectetur.</p>
    <div style="left:40px;top:170px;font-size:20px;font-weight:700;color:var(--royal)">12%</div>
    <p class="copy" style="left:40px;top:196px;width:110px">Lorem ipsum dolor sit amet consectetur.</p>
    <div style="left:420px;top:80px;font-size:20px;font-weight:700;color:var(--sky)">20%</div>
    <p class="copy" style="left:420px;top:106px;width:110px">Lorem ipsum dolor sit amet consectetur.</p>
    <div style="left:420px;top:170px;font-size:20px;font-weight:700;color:var(--navy)">36%</div>
    <p class="copy" style="left:420px;top:196px;width:110px">Lorem ipsum dolor sit amet consectetur.</p>
    <div class="brand sm foot"><i></i>TRELUM</div>
    <div class="pgnum">15</div>
  </section>

  <section class="slide">
    <div class="kicker" style="left:0;top:22px;width:560px;text-align:center;font-size:14px">Chart <span class="accent">Slide</span></div>
    <svg style="left:24px;top:60px" width="310" height="190" viewBox="0 0 310 190">
      <g stroke="#e3e7ef"><line x1="20" y1="20" x2="310" y2="20"/><line x1="20" y1="65" x2="310" y2="65"/><line x1="20" y1="110" x2="310" y2="110"/><line x1="20" y1="155" x2="310" y2="155"/></g>
      <g fill="#517ed8"><rect x="35" y="80" width="10" height="75"/><rect x="95" y="50" width="10" height="105"/><rect x="155" y="100" width="10" height="55"/><rect x="215" y="35" width="10" height="120"/><rect x="275" y="70" width="10" height="85"/></g>
      <g fill="#6ea6fa"><rect x="48" y="110" width="10" height="45"/><rect x="108" y="90" width="10" height="65"/><rect x="168" y="75" width="10" height="80"/><rect x="228" y="95" width="10" height="60"/><rect x="288" y="115" width="10" height="40"/></g>
      <g fill="#203390"><rect x="61" y="125" width="10" height="30"/><rect x="121" y="115" width="10" height="40"/><rect x="181" y="120" width="10" height="35"/><rect x="241" y="105" width="10" height="50"/></g>
      <g font-size="7" font-family="Work Sans" fill="#4a4f5c"><text x="40" y="170">Q1</text><text x="100" y="170">Q2</text><text x="160" y="170">Q3</text><text x="220" y="170">Q4</text><text x="280" y="170">Q5</text></g>
    </svg>
    <div class="stat" style="left:360px;top:70px;width:176px;height:52px"><b>160,000</b><span>Lorem ipsum dolor sit amet</span></div>
    <div class="stat" style="left:360px;top:132px;width:176px;height:52px"><b>13,000</b><span>Lorem ipsum dolor sit amet</span></div>
    <div class="stat" style="left:360px;top:194px;width:176px;height:52px"><b>150</b><span>Lorem ipsum dolor sit amet</span></div>
    <div class="brand sm foot"><i></i>TRELUM</div>
    <div class="pgnum">16</div>
  </section>

  <section class="slide">
    <div style="left:0;top:0;width:170px;height:315px;background:var(--navy)"></div>
    <div style="left:20px;top:30px;font-size:13px;font-weight:800;color:#fff;line-height:1.1">LOCATION<br><span style="font-weight:400;color:var(--sky)">Slide</span></div>
    <div style="left:20px;top:80px;width:130px;display:flex;flex-direction:column;gap:7px">
      <div class="btn" style="position:static;justify-content:flex-start;padding-left:8px;background:var(--royal)">Lorem ipsum dolor sit</div>
      <div class="btn" style="position:static;justify-content:flex-start;padding-left:8px;background:var(--royal)">Consectetur adipiscing</div>
      <div class="btn" style="position:static;justify-content:flex-start;padding-left:8px;background:var(--royal)">Vivamus lacus nisi</div>
      <div class="btn" style="position:static;justify-content:flex-start;padding-left:8px;background:var(--royal)">Cursus et eleifend</div>
      <div class="btn" style="position:static;justify-content:flex-start;padding-left:8px;background:var(--royal)">Commodo id lorem</div>
    </div>
    <div class="photo map" role="img" aria-label="World map with highlighted office regions" style="left:190px;top:40px;width:350px;height:220px"></div>
    <div class="brand sm foot light"><i></i>TRELUM</div>
    <div class="pgnum">17</div>
  </section>

  <section class="slide">
    <div style="left:0;top:0;width:170px;height:315px;background:var(--pale)"></div>
    <div class="kicker" style="left:20px;top:40px;font-size:13px">Comparaison</div>
    <div class="accent" style="left:20px;top:56px;font-size:12px">Slide</div>
    <p class="copy" style="left:20px;top:84px;width:130px">Lorem ipsum dolor sit amet, consectetur adipiscing elit. Vivamus lacus nisi, cursus et eleifend quis, commodo id lorem.</p>
    <div class="card" style="left:186px;top:30px;width:110px;height:250px"><div class="num">1</div><h4>TITLE</h4><h5>GOES HERE</h5><p class="copy light" style="padding:0 10px">Lorem ipsum dolor sit amet, consectetur adipiscing elit nisi.</p></div>
    <div class="card" style="left:306px;top:30px;width:110px;height:250px;background:var(--royal)"><div class="num">2</div><h4>TITLE</h4><h5>GOES HERE</h5><p class="copy light" style="padding:0 10px">Lorem ipsum dolor sit amet, consectetur adipiscing elit nisi.</p></div>
    <div class="card" style="left:426px;top:30px;width:110px;height:250px"><div class="num">3</div><h4>TITLE</h4><h5>GOES HERE</h5><p class="copy light" style="padding:0 10px">Lorem ipsum dolor sit amet, consectetur adipiscing elit nisi.</p></div>
    <div class="brand sm foot"><i></i>TRELUM</div>
    <div class="pgnum">18</div>
  </section>

  <section class="slide wide">
    <div class="photo mono" role="img" aria-label="Monochrome regatta fleet on the water" style="left:0;top:0;width:560px;height:315px"></div>
    <div style="left:330px;top:0;width:200px;height:280px;background:var(--navy)"></div>
    <div class="brand lg light" style="left:370px;top:30px"><i></i>TRELUM</div>
    <div style="left:330px;top:78px;width:200px;text-align:center;font-size:20px;font-weight:700;color:#fff">Thank You!</div>
    <div style="left:330px;top:104px;width:200px;text-align:center;font-size:6.5px;color:var(--sky)">For Your Time and Attention</div>
    <div style="left:330px;top:140px;width:200px;text-align:center;font-size:7px;font-weight:700;color:#fff">CONTACT US</div>
    <p class="copy light" style="left:350px;top:158px;width:160px;text-align:center">+00 123 456 789<br>hello@trelum.com<br>www.trelum.com<br>12 Harbour Road, Portside</p>
    <div style="left:380px;top:226px;width:100px;height:2px;background:var(--sky)"></div>
    <div class="bracket" style="left:530px;top:0;border-color:var(--sky)"></div>
    <div class="pgnum">19</div>
  </section>

</main>
</body>
</html>
```